Business Card

I would like a business card with a picture of my husband and I that is unique and professional.

Industry/Entity Type

Business

Font styles to use
Serif

```html
<!DOCTYPE html>
<html lang="en">
<head>
<meta charset="utf-8">
<title>Nadia Brooks — Business Card</title>
<link rel="stylesheet" href="https://fonts.googleapis.com/css2?family=Cinzel:wght@400;600&family=EB+Garamond:wght@400;500&display=swap">
<style>
  :root {
    --backdrop: #7b7b7b;
    --wine: #8a1a20;
    --wine-deep: #6e1217;
    --gold: #e0a93a;
    --gold-light: #f6d77a;
    --gold-dark: #b47a1c;
    --cream: #fbf3dc;
    --ink: #1c0c0c;
    --slate: #3a3a3a;
    --paper: #ffffff;
    --red-edge: #c0121a;
  }
  * { box-sizing: border-box; margin: 0; padding: 0; }
  html, body { width: 1200px; height: 900px; overflow: hidden; }
  body { background: var(--backdrop); position: relative; }

  .card {
    position: absolute;
    left: 290px;
    width: 620px;
    height: 354px;
    box-shadow: 0 10px 28px rgba(0,0,0,.35);
    overflow: hidden;
  }
  .card--front { top: 60px; background: var(--wine); }
  .card--back  { top: 478px; background: var(--red-edge); }

  /* gold frame */
  .frame {
    position: absolute;
    inset: 12px;
    border: 8px solid transparent;
    border-image: linear-gradient(135deg, var(--gold-dark), var(--gold-light) 35%, var(--gold) 60%, var(--cream) 80%, var(--gold-dark)) 1;
  }
  .frame::after {
    content: "";
    position: absolute;
    inset: 2px;
    border: 1px solid rgba(251,243,220,.6);
  }
  .card--front .frame-fill { position: absolute; inset: 20px; background: linear-gradient(160deg, var(--wine) 0%, var(--wine-deep) 100%); }

  .name {
    position: absolute;
    left: 56px; top: 50px;
    font-family: "Cinzel", serif;
    font-weight: 400;
    font-size: 36px;
    letter-spacing: 1px;
    color: var(--gold);
  }
  .title {
    position: absolute;
    left: 56px; top: 96px;
    font-family: "EB Garamond", serif;
    font-size: 20px;
    color: var(--ink);
  }
  .divider { position: absolute; left: 80px; top: 126px; width: 360px; height: 14px; }

  .contact {
    position: absolute;
    left: 80px;
    display: flex;
    align-items: center;
    gap: 12px;
    font-family: "EB Garamond", serif;
    font-size: 24px;
    color: var(--gold);
  }
  .contact--phone { top: 168px; }
  .contact--email { top: 212px; }
  .contact-icon { width: 28px; height: 28px; flex: none; }

  .portrait {
    position: absolute;
    left: 395px; top: 20px;
    width: 205px; height: 314px;
    background: linear-gradient(170deg, #6b5a55 0%, #8f8b8f 45%, #a9a8ad 70%, #7d7a80 100%);
  }

  .card--back .paper {
    position: absolute;
    inset: 20px;
    background: radial-gradient(ellipse at center, var(--paper) 70%, #fff6e0 100%);
  }
  .brand {
    position: absolute;
    left: 0; right: 0; top: 108px;
    display: flex;
    flex-direction: column;
    align-items: center;
    gap: 16px;
  }
  .brand-mark {
    width: 64px; height: 64px;
    border-radius: 50%;
    background: var(--gold);
  }
  .brand-name {
    font-family: "Cinzel", serif;
    font-weight: 600;
    font-size: 22px;
    letter-spacing: 2px;
    color: var(--slate);
    text-transform: uppercase;
  }
  .brand-rule { width: 380px; height: 14px; }
</style>
</head>
<body>

  <section class="card card--front">
    <div class="frame-fill"></div>
    <div class="frame"></div>

    <h1 class="name">NADIA BROOKS</h1>
    <p class="title">Professional Mentorship Strategist</p>
    <svg class="divider" viewBox="0 0 360 14" aria-hidden="true">
      <line x1="0" y1="7" x2="360" y2="7" stroke="var(--gold)" stroke-width="1.2"/>
      <rect x="175" y="2" width="10" height="10" transform="rotate(45 180 7)" fill="var(--gold)"/>
    </svg>

    <p class="contact contact--phone">
      <svg class="contact-icon" viewBox="0 0 28 28" aria-hidden="true">
        <circle cx="14" cy="14" r="14" fill="var(--gold)"/>
        <path d="M9 7.5c1-.6 2-.3 2.4.6l1 2.3c.3.7.1 1.4-.5 1.8l-.9.6c.7 1.6 1.9 2.9 3.5 3.7l.7-.9c.5-.6 1.2-.7 1.8-.4l2.2 1.1c.9.5 1.1 1.5.5 2.4-.8 1.2-2.1 1.8-3.5 1.4-4-1.2-6.9-4.3-7.9-8.3-.3-1.5.2-3 1.2-3.7z" fill="var(--cream)"/>
      </svg>
      <span>312-555-0148 Direct</span>
    </p>
    <p class="contact contact--email">
      <svg class="contact-icon" viewBox="0 0 28 28" aria-hidden="true">
        <circle cx="14" cy="14" r="14" fill="var(--gold)"/>
        <rect x="7" y="9" width="14" height="10" rx="1" fill="var(--cream)"/>
        <path d="M7.5 9.5 14 15l6.5-5.5" fill="none" stroke="var(--gold-dark)" stroke-width="1.2"/>
      </svg>
      <span>NadiaBrooks@example.com</span>
    </p>

    <div class="portrait" role="img" aria-label="Portrait photograph of the couple in grey business attire"></div>
  </section>

  <section class="card card--back">
    <div class="frame"></div>
    <div class="paper"></div>
    <div class="brand">
      <div class="brand-mark" aria-hidden="true"></div>
      <p class="brand-name">Brooks Leadership Development</p>
      <svg class="brand-rule" viewBox="0 0 380 14" aria-hidden="true">
        <line x1="0" y1="7" x2="380" y2="7" stroke="var(--slate)" stroke-width="1"/>
        <rect x="185" y="2" width="10" height="10" transform="rotate(45 190 7)" fill="var(--slate)"/>
      </svg>
    </div>
  </section>

</body>
</html>
```